Brightwell Rx Pass reinvent our website.

Our Website is outdated and needs an overhaul, in every aspect. We assist individuals that have little or no prescription coverage and allow them to receive a discount ranging from 33% up to 78% for free. In the beginning we utilized pharmacies to spread the word, but times have a changed. We are looking for a modern and clean site. We are open to anything, image, logo etc.

Target Market(s)

Anyone regardless of residency, age or income. This program is designed to assist those that have NO prescription coverage or for those whose particular prescription may not be covered by insurance.

Industry/Entity Type

Pharmaceutical

Coding

Coded - Design and coding required

Number of Pages Required

4 page

Requirements
Must have
• -The two MUST haves are the pharmacy locators & drug pricing. If you can combine the 2, even better.
• -a ongoing counter/tally on the 1stpage reflecting the amount of money we are saving customers. http://plumtreemarket.example/item/animated-counters-v-20-edge-animate-collection/full_screen_preview/52970314
• -on a smart phone the ability to view the information that is needed to get the actual discount for the medication.
Nice to have
• animated tutorial showing how to use the card
• health blog

```html
<!DOCTYPE html>
<html lang="en">
<head>
<meta charset="utf-8">
<title>Brightwell Rx Pass – Prescription Savings</title>
<link rel="stylesheet" href="https://fonts.googleapis.com/css2?family=Open+Sans:wght@300;400;600;700;800&family=Arimo:ital,wght@0,400;0,700;1,400&display=swap">
<style>
  :root {
    --red: #f2352f;
    --red-deep: #e3121b;
    --blue: #2f6aa5;
    --navy: #0d4686;
    --sky: #5b98c4;
    --band-top: #4a9bd1;
    --band-bottom: #2d5c9b;
    --ink: #222;
    --ink-soft: #444;
    --grey-bar: #dcdcdc;
    --rule: #cfcfcf;
    --white: #fff;
    --map: #d9d9d9;
  }
  * { box-sizing: border-box; margin: 0; padding: 0; }
  html, body { width: 1200px; height: 2293px; overflow: hidden; }
  body { position: relative; background: var(--white); font-family: "Arimo", Arial, sans-serif; color: var(--ink); }

  /* header */
  .site-header { position: absolute; left: 0; top: 0; width: 1200px; height: 112px; background: var(--white); }
  .brand { position: absolute; left: 61px; top: 38px; display: flex; align-items: center; gap: 12px; }
  .brand-dot { width: 34px; height: 34px; border-radius: 50%; background: var(--navy); }
  .brand-name { font-family: "Open Sans", sans-serif; font-weight: 700; font-size: 27px; color: var(--navy); letter-spacing: -0.3px; }
  .util-links { position: absolute; top: 20px; left: 925px; display: flex; align-items: center; font-size: 15px; color: var(--ink-soft); }
  .util-signup { width: 79px; height: 31px; border: 1.5px solid var(--red); border-radius: 16px; display: flex; align-items: center; justify-content: center; }
  .util-login { margin-left: 38px; }
  .util-help { margin-left: 37px; }
  .main-nav { position: absolute; top: 72px; left: 0; width: 1200px; font-size: 15px; color: var(--ink); }
  .main-nav span { position: absolute; white-space: nowrap; }

  /* search band */
  .search-band { position: absolute; left: 0; top: 112px; width: 1200px; height: 111px; background: linear-gradient(#4c92c8, #2a6aa6); }
  .field { position: absolute; top: 35px; height: 41px; background: var(--white); border-radius: 3px; padding-left: 14px; display: flex; align-items: center; font-size: 14px; font-family: "Open Sans", sans-serif; }
  .field-drug { left: 61px; width: 431px; color: #333; font-weight: 700; }
  .field-place { left: 529px; width: 431px; color: #aaa; }
  .search-btn { position: absolute; left: 980px; top: 35px; width: 159px; height: 43px; background: var(--red); border-radius: 2px; color: var(--white); font-family: "Open Sans", sans-serif; font-weight: 800; font-size: 21px; display: flex; align-items: center; justify-content: center; gap: 8px; }

  /* hero */
  .hero { position: absolute; left: 0; top: 223px; width: 1200px; height: 439px; background: linear-gradient(135deg, #c9d3dc 0%, #a9b9c6 40%, #dfe4e8 70%, #b8c4ce 100%); }
  .hero-frame { position: absolute; left: 226px; top: 115px; width: 760px; height: 131px; }
  .hero-title { position: absolute; left: 0; top: 0; width: 1200px; height: 439px; display: flex; align-items: center; justify-content: center; padding-bottom: 75px; font-family: "Open Sans", sans-serif; font-weight: 800; font-size: 51px; color: var(--white); text-shadow: 0 2px 6px rgba(0,0,0,.35); }

  /* how it works */
  .chevron { position: absolute; left: 597px; top: 749px; }
  .section-title { position: absolute; top: 800px; left: 0; width: 1200px; text-align: center; font-family: "Open Sans", sans-serif; font-weight: 300; font-size: 49px; color: var(--ink); }
  .tab-rule { position: absolute; left: 147px; top: 958px; width: 923px; height: 1px; background: var(--rule); }
  .tab { position: absolute; top: 914px; height: 44px; color: var(--white); font-weight: 700; font-size: 14px; display: flex; align-items: center; justify-content: center; }
  .tab-medication { left: 440px; width: 138px; background: var(--red); }
  .tab-medication::after { content: ""; position: absolute; bottom: -8px; left: 61px; border: 8px solid transparent; border-bottom: 0; border-top-color: var(--red); }
  .tab-pharmacy { left: 598px; width: 192px; background: var(--blue); }

  .step { position: absolute; top: 1040px; width: 300px; text-align: center; }
  .step-icon { width: 118px; height: 118px; border-radius: 50%; margin: 0 auto; display: flex; align-items: center; justify-content: center; }
  .step-title { font-family: "Open Sans", sans-serif; font-size: 23px; line-height: 29px; letter-spacing: .6px; color: var(--ink); margin-top: 16px; }
  .step-text { font-size: 13.5px; line-height: 20px; color: var(--ink-soft); margin-top: 14px; }

  .price-bar { position: absolute; left: 139px; top: 1367px; width: 923px; height: 71px; background: var(--grey-bar); }
  .price-bar-label { position: absolute; left: 22px; top: 26px; font-size: 16px; color: #333; }
  .go-btn { position: absolute; left: 792px; top: 16px; width: 113px; height: 40px; background: var(--red-deep); color: var(--white); font-family: "Open Sans", sans-serif; font-size: 22px; display: flex; align-items: center; justify-content: center; }

  /* savings band */
  .consultants { position: absolute; left: 0; top: 1564px; width: 1200px; height: 354px; background: linear-gradient(var(--band-top), var(--band-bottom)); }
  .quote-mark { position: absolute; left: 580px; top: -25px; width: 50px; height: 50px; border-radius: 50%; background: var(--red); border: 3px solid var(--white); color: var(--white); font-family: "Open Sans", sans-serif; font-weight: 800; font-size: 34px; display: flex; align-items: center; justify-content: center; padding-top: 10px; }
  .savings-title { position: absolute; top: 37px; left: 0; width: 1200px; text-align: center; color: var(--white); font-size: 23px; font-weight: 400; }
  .savings-count { font-weight: 700; }
  .person { position: absolute; top: 105px; width: 150px; text-align: center; color: var(--white); }
  .person-photo { width: 144px; height: 144px; border-radius: 50%; margin: 0 auto; border: 3px solid #8fbbe0; background: radial-gradient(circle at 50% 40%, #6a5a4c, #2b2622); }
  .person-name { font-size: 16px; margin-top: 19px; }
  .person-rule { width: 118px; height: 1px; background: rgba(255,255,255,.55); margin: 8px auto 0; }
  .person-status { font-size: 13.5px; font-style: italic; margin-top: 6px; display: flex; align-items: center; justify-content: center; gap: 6px; }
  .status-dot { width: 13px; height: 13px; border-radius: 50%; background: #b9c2cc; }
  .status-dot.online { background: #6fcf2a; }

  .map { position: absolute; left: 0; top: 1918px; width: 1200px; height: 325px; background: linear-gradient(135deg, #e3e3e3, var(--map) 50%, #cfcfcf); }
  .site-footer { position: absolute; left: 0; top: 2243px; width: 1200px; height: 50px; background: var(--red); color: var(--white); font-size: 13px; display: flex; align-items: center; justify-content: center; }
</style>
</head>
<body>

<header class="site-header">
  <div class="brand"><span class="brand-dot"></span><span class="brand-name">Brightwell Rx Pass</span></div>
  <div class="util-links">
    <span class="util-signup">Sign Up</span>
    <span class="util-login">Log In</span>
    <span class="util-help">Help</span>
  </div>
  <nav class="main-nav">
    <span style="left:425px">Prescription Savings Card</span>
    <span style="left:648px">Resources</span>
    <span style="left:770px">Partner Program</span>
    <span style="left:940px">Newsroom</span>
    <span style="left:1062px">About Us</span>
  </nav>
</header>

<section class="search-band">
  <div class="field field-drug">Type a drug to find it cheaper, near you.</div>
  <div class="field field-place">City, State or ZIP</div>
  <div class="search-btn">
    <svg width="24" height="24" viewBox="0 0 24 24"><circle cx="10" cy="10" r="7" fill="none" stroke="#111" stroke-width="3.5"/><line x1="15" y1="15" x2="22" y2="22" stroke="#111" stroke-width="4" stroke-linecap="round"/></svg>
    SEARCH
  </div>
</section>

<section class="hero" role="img" aria-label="Hands holding blister packs of assorted pills and capsules">
  <svg class="hero-frame" viewBox="0 0 760 131" fill="none">
    <path d="M390 3 H66 A63 63 0 0 0 66 128 H390" stroke="#1d5aa8" stroke-width="4"/>
    <path d="M420 3 H694 A63 63 0 0 1 694 128 H420" stroke="#e63a3a" stroke-width="4"/>
  </svg>
  <div class="hero-title">Prescription Medication?</div>
</section>

<svg class="chevron" width="40" height="24" viewBox="0 0 40 24"><polyline points="2,2 20,21 38,2" fill="none" stroke="#bbb" stroke-width="3"/></svg>
<h1 class="section-title">Prescription Medication?</h1>

<div class="tab-rule"></div>
<div class="tab tab-medication">Medication</div>
<div class="tab tab-pharmacy">Pharmacy Locator</div>

<div class="step" style="left:130px">
  <div class="step-icon" style="background:var(--sky)">
    <svg width="60" height="60" viewBox="0 0 60 60" fill="none" stroke="#fff" stroke-width="4" stroke-linecap="round"><rect x="18" y="18" width="14" height="28" rx="2" transform="rotate(45 25 32)"/><line x1="36" y1="24" x2="46" y2="14"/><line x1="41" y1="9" x2="51" y2="19"/><line x1="14" y1="46" x2="8" y2="52"/></svg>
  </div>
  <div class="step-title">Search Your<br>Medication</div>
  <div class="step-text">Enter the Name of Your Prescription<br>and Your Location - eg. Drug, Dose,<br>Quantity, City or ZIP Code.</div>
</div>

<div class="step" style="left:448px">
  <div class="step-icon" style="background:var(--red)">
    <svg width="60" height="60" viewBox="0 0 60 60" fill="none" stroke="#fff" stroke-width="5"><rect x="6" y="20" width="48" height="20" rx="10" transform="rotate(-45 30 30)"/><line x1="24" y1="24" x2="36" y2="36"/></svg>
  </div>
  <div class="step-title" style="margin-top:22px">Compare Prices<br>Near You</div>
  <div class="step-text">See Discounted Prices at Pharmacies<br>Nearby and Choose the Best One.</div>
</div>

<div class="step" style="left:767px">
  <div class="step-icon" style="background:var(--navy)">
    <svg width="64" height="64" viewBox="0 0 64 64" fill="none"><circle cx="27" cy="27" r="17" stroke="#fff" stroke-width="4"/><line x1="40" y1="40" x2="54" y2="54" stroke="#fff" stroke-width="6" stroke-linecap="round"/><rect x="20" y="19" width="14" height="17" rx="2" fill="#f4d35e"/><rect x="22" y="16" width="10" height="4" fill="#fff"/><path d="M27 23v9M22.5 27.5h9" stroke="#2a8f4a" stroke-width="2.5"/></svg>
  </div>
  <div class="step-title" style="margin-top:22px">Show Your Card<br>and Save</div>
  <div class="step-text">Save 33% to 78% at the counter,<br>free for everyone.</div>
</div>

<div class="price-bar">
  <span class="price-bar-label">Begin pricing by searching for a drug.</span>
  <span class="go-btn">GO</span>
</div>

<section class="consultants">
  <div class="quote-mark">“</div>
  <h2 class="savings-title">Our members have saved <span class="savings-count">$4,827,316</span> on prescriptions so far</h2>
  <div class="person" style="left:170px"><div class="person-photo" role="img" aria-label="Pharmacist portrait"></div><div class="person-name">Dario Lenk</div><div class="person-rule"></div><div class="person-status"><span class="status-dot online"></span>online</div></div>
  <div class="person" style="left:353px"><div class="person-photo" role="img" aria-label="Pharmacist portrait"></div><div class="person-name">Dario Lenk</div><div class="person-rule"></div><div class="person-status"><span class="status-dot"></span>offline</div></div>
  <div class="person" style="left:535px"><div class="person-photo" role="img" aria-label="Pharmacist portrait"></div><div class="person-name">Dario Lenk</div><div class="person-rule"></div><div class="person-status"><span class="status-dot"></span>offline</div></div>
  <div class="person" style="left:715px"><div class="person-photo" role="img" aria-label="Pharmacist portrait"></div><div class="person-name">Dario Lenk</div><div class="person-rule"></div><div class="person-status"><span class="status-dot"></span>offline</div></div>
  <div class="person" style="left:893px"><div class="person-photo" role="img" aria-label="Pharmacist portrait"></div><div class="person-name">Dario Lenk</div><div class="person-rule"></div><div class="person-status"><span class="status-dot"></span>offline</div></div>
</section>

<div class="map" role="img" aria-label="Street map showing nearby pharmacy locations"></div>

<footer class="site-footer">© 2015 Copyright - Brightwell Rx Pass. All rights reserved</footer>

</body>
</html>
```